Banner Ad Design Project for responsive website

Looking to update the main banner on my website www.vowlantern.example but it will be for our new responsive website, you can see here http://www.vowlantern.example/dev/
Banner should be 300 px high by1920 pix wide
Please contact me with any questions
Should include:
All the text from the existing banner ie
Bridal Show
THE FIRST 50 BRIDES WILL GET A CHANCE TO WIN $25000
Honeymoon Cruise Giveaway
"Pick Your Perfect Gown" casting call
Banner should be 1920 pix wide
Final delivery will require layered psd file and all fonts

Target Market(s)

Brides

Industry/Entity Type

Call

Requirements
Must have
• All the text from the existing banner ie
• Bridal Show
• THE FIRST 50 BRIDES WILL GET A CHANCE TO WIN $25000
• Honeymoon Cruise Giveaway
• "Pick Your Perfect Gown" casting call
• Banner should be 1920 pix wide
Nice to have
• The look and feel of our postcard, see attached
Should not have
• Any specifics to any date/time/location as the banner will be online all the time and the specifics for each show will be different

```html
<!DOCTYPE html>
<html lang="en">
<head>
<meta charset="utf-8">
<title>Bridal Show Banners</title>
<link rel="stylesheet" href="https://fonts.googleapis.com/css2?family=Great+Vibes&family=Open+Sans:wght@400;700&display=swap">
<style>
  :root {
    --stage: #e9e9e9;
    --stage-light: #fbfbfb;
    --white: #ffffff;
    --ink: #111111;
    --ring: #f2d64a;
    --forest-dark: #1c2312;
    --forest-mid: #3e4a22;
    --forest-light: #6b6a3a;
    --skin: #8a6f5c;
    --brick-dark: #2a1a14;
    --brick-mid: #4f3227;
    --brick-light: #6d4a3a;
    --sea-top: #bfe3f0;
    --sea-bottom: #1f8fb5;
    --ornament: rgba(255,255,255,0.25);
  }
  * { margin: 0; padding: 0; box-sizing: border-box; }
  html, body { width: 1200px; height: 1000px; overflow: hidden; }
  body {
    position: relative;
    background: radial-gradient(ellipse at 50% 45%, var(--stage-light) 0%, var(--stage) 75%);
    font-family: "Open Sans", sans-serif;
    color: var(--white);
  }
  .banner {
    position: absolute;
    left: 63px;
    width: 1072px;
    height: 167px;
    overflow: hidden;
  }
  .banner--garden { top: 182px; }
  .banner--street { top: 569px; }
  .banner__photo { position: absolute; inset: 0; }
  .banner--garden .banner__photo {
    background: linear-gradient(90deg, var(--forest-dark) 0%, var(--forest-mid) 45%, var(--forest-light) 70%, var(--skin) 85%, var(--forest-mid) 100%);
  }
  .banner--street .banner__photo {
    background: linear-gradient(90deg, var(--brick-dark) 0%, var(--brick-mid) 30%, var(--brick-light) 50%, var(--brick-mid) 70%, var(--brick-dark) 100%);
  }
  .show-block {
    position: absolute;
    width: 290px;
    text-align: center;
  }
  .banner--garden .show-block { left: 28px; top: 10px; }
  .banner--street .show-block { left: 392px; top: 10px; }
  .ornament {
    display: block;
    margin: 0 auto;
    width: 110px;
    height: 14px;
    background: var(--ornament);
    border-radius: 7px;
  }
  .show-title {
    position: relative;
    display: inline-block;
    font-family: "Great Vibes", cursive;
    font-size: 50px;
    line-height: 52px;
    font-weight: 400;
  }
  .ring {
    position: absolute;
    right: -16px;
    top: 24px;
  }
  .show-lead {
    font-size: 12.5px;
    line-height: 16px;
    text-transform: uppercase;
    padding-bottom: 4px;
    border-bottom: 1px dotted rgba(255,255,255,0.7);
    margin: 0 4px;
  }
  .show-prize {
    font-size: 29px;
    font-weight: 700;
    line-height: 36px;
    margin-bottom: 2px;
  }
  .cruise-badge {
    position: absolute;
    border: 2px solid var(--white);
    border-radius: 50%;
    background: linear-gradient(180deg, var(--sea-top) 0%, var(--sea-bottom) 100%);
  }
  .banner--garden .cruise-badge { left: 356px; top: 12px; width: 118px; height: 118px; clip-path: inset(0 0 14% 0); }
  .banner--street .cruise-badge { left: 65px; top: 35px; width: 76px; height: 76px; clip-path: inset(0 0 16% 0); }
  .cruise-name {
    position: absolute;
    font-family: "Great Vibes", cursive;
    font-size: 19px;
    line-height: 21px;
  }
  .banner--garden .cruise-name { left: 479px; top: 55px; }
  .label {
    position: absolute;
    background: var(--white);
    color: var(--ink);
    border-radius: 3px;
    font-size: 13px;
    line-height: 22px;
    padding: 0 6px;
    white-space: nowrap;
  }
  .banner--garden .label--casting { left: 359px; top: 121px; }
  .banner--street .label--cruise {
    left: 137px; top: 72px; width: 220px;
    font-family: "Great Vibes", cursive;
    font-size: 18px;
    padding-left: 10px;
  }
  .banner--street .label--casting { left: 738px; top: 73px; }
</style>
</head>
<body>

  <section class="banner banner--garden">
    <div class="banner__photo" role="img" aria-label="Soft-focus photo of a couple embracing in a leafy garden"></div>
    <div class="show-block">
      <span class="ornament" role="img" aria-label="Decorative flourish"></span>
      <h1 class="show-title">Bridal Show
        <svg class="ring" width="22" height="26" viewBox="0 0 22 26" aria-hidden="true"><circle cx="10" cy="15" r="9" fill="none" stroke="var(--ring)" stroke-width="2"/><path d="M16 4 l3 -2 l2 3 l-3 2 z" fill="#bfe6f5"/></svg>
      </h1>
      <p class="show-lead">The first 50 brides will get a chance to</p>
      <p class="show-prize">WIN $25000</p>
      <span class="ornament" role="img" aria-label="Decorative flourish"></span>
    </div>
    <div class="cruise-badge" role="img" aria-label="Photo of a white cruise ship on turquoise sea"></div>
    <p class="cruise-name">Honeymoon<br>Cruise Giveaway</p>
    <p class="label label--casting">Open Casting Call "Pick Your Perfect Gown"</p>
  </section>

  <section class="banner banner--street">
    <div class="banner__photo" role="img" aria-label="Blurred photo of a couple under an umbrella in front of a brick building"></div>
    <p class="label label--cruise">Honeymoon Cruise Giveaway</p>
    <div class="cruise-badge" role="img" aria-label="Photo of a white cruise ship on turquoise sea"></div>
    <div class="show-block">
      <span class="ornament" role="img" aria-label="Decorative flourish"></span>
      <h1 class="show-title">Bridal Show
        <svg class="ring" width="22" height="26" viewBox="0 0 22 26" aria-hidden="true"><circle cx="10" cy="15" r="9" fill="none" stroke="var(--ring)" stroke-width="2"/><path d="M16 4 l3 -2 l2 3 l-3 2 z" fill="#bfe6f5"/></svg>
      </h1>
      <p class="show-lead">The first 50 brides will get a chance to</p>
      <p class="show-prize">WIN $25000</p>
      <span class="ornament" role="img" aria-label="Decorative flourish"></span>
    </div>
    <p class="label label--casting">Open Casting Call "Pick Your Perfect Gown"</p>
  </section>

</body>
</html>
```